Security Officer Training Certifications POSTCARD

We need Post Card Design
-Front and Back
-In Compliance with KETTLE MAIL for upload!
-For Oversized and Jumbo Size Cards (kettle mails)

Our Company:
www.brightwallreadinessinstitute.org (FOR IDEAS)

We provide Corporate Security Officer/Criminal Justice/Police Tactics Training for Private Companies that have a security department and officers.

We provide:
Handcuffing certifications
Pepper Spray
Compliance Training
Instructor Training
California Guard Card

FRONT DESIGN TO BE VERY CATCH!
Back of Card List of Services/Menu

Our Card to display powerful image for a Security Officer Department
Traits in Pic and Deigns
VALUE
COMPETITIVE EDGE
PROFESSIONAL GROWTH
QUALITY
PROFICIENT/EFFECTIVE SECURITY OFFICERS
TACTICAL OFFICERS
PROFESSIONALISM
EXPERTS
INDUSTRY LEADERS
READINESS

Target Market(s)

Proprietary Security Officer Department. Agencies that hire their own guard force.
It will be owners of security guard companies, Security Directors, manager

Industry/Entity Type

Security

Requirements
Must have
• GREAT FROM OF CARD PICTURE that encompasses
• Corporate Security Officers
• MUST HAVE A COOL LOOK!
• Professionalism
• Tactical
• The best
• Upgrade skills
• BACK of Card:
• Like list of services with pics and cool stuff
• PICS of Security Officer /Police Professionals
• with great backgrounds!
• COOL
• BACK OF CARD
• Space to have address of receipient
• space for post age
• in ACCORDANCE with KETTLE MAILS to upload...

```html
<!DOCTYPE html>
<html lang="en">
<head>
<meta charset="utf-8">
<title>Security Corporate Training Postcard</title>
<link rel="stylesheet" href="https://fonts.googleapis.com/css2?family=Oswald:wght@400;500;600&family=Montserrat:wght@700;800&family=Open+Sans:wght@400;600;700&display=swap">
<style>
:root{
  --royal:#2e3192;
  --navy:#1c1d4f;
  --ink:#111;
  --paper:#f3f3f4;
  --white:#fff;
  --gold:#c9a24a;
  --silver:#c7c9ce;
  --line:#c9c9c9;
  --bg:#e9e9ec;
}
*{box-sizing:border-box;margin:0;padding:0}
html,body{width:1100px;height:1200px;overflow:hidden;background:var(--bg)}
.postcard{position:absolute;left:118px;width:864px;height:560px;box-shadow:0 3px 10px rgba(0,0,0,.25);overflow:hidden}
.front{top:30px;background:var(--paper)}
.back{top:610px;background:var(--white)}

/* brand */
.brand-mark{position:absolute;z-index:2;display:flex;flex-direction:column;align-items:center;justify-content:flex-start;gap:4px;text-align:center;font-family:'Open Sans',sans-serif;font-weight:700;color:var(--royal)}
.brand-mark .dot{border-radius:50%;border:4px solid var(--royal);background:var(--white);flex:none}
.front .brand-mark{left:18px;top:20px;width:150px;font-size:12px;line-height:1.2}
.front .brand-mark .dot{width:64px;height:64px}

/* front header */
.front-title{position:absolute;left:170px;top:16px;width:624px;text-align:center;white-space:nowrap;font-family:'Oswald',sans-serif;font-weight:600;font-size:45px;letter-spacing:0;color:var(--royal);line-height:52px}
.front-sub{position:absolute;left:170px;top:74px;width:624px;text-align:center;white-space:nowrap;font-family:'Oswald',sans-serif;font-weight:500;font-size:20px;color:var(--ink);line-height:26px}
.url-band{position:absolute;left:0;top:128px;width:864px;height:32px;background:var(--navy);font-family:'Oswald',sans-serif;color:var(--white)}
.url-band .url{position:absolute;left:265px;top:5px;font-size:16px}
.url-band .license{position:absolute;right:78px;top:8px;font-size:11px}

.hero-photo{position:absolute;left:0;top:160px;width:864px;height:310px;
  background:radial-gradient(ellipse at 30% 60%,#d9dadd 0%,#a7a9ae 55%,#6c6e74 100%)}
.hero-officer{position:absolute;left:490px;top:150px;width:370px;height:320px;
  background:linear-gradient(180deg,#2b2f3a 0%,#3c4250 45%,#1b1d24 100%);border-radius:140px 140px 0 0;opacity:.85}
.provide{position:absolute;left:34px;top:192px;font-family:'Montserrat',sans-serif;font-weight:800;color:var(--navy);font-size:25px}
.services{position:absolute;left:38px;top:232px;list-style:none}
.services li{display:flex;align-items:center;gap:10px;height:40px;font-family:'Montserrat',sans-serif;font-weight:800;font-size:23px;color:var(--royal);white-space:nowrap}
.services svg{width:20px;height:20px}

.onsite-band{position:absolute;left:0;top:470px;width:864px;height:42px;background:var(--navy);color:var(--white);font-family:'Oswald',sans-serif;font-size:16px}
.onsite-band p{position:absolute;left:158px;top:10px;white-space:nowrap}
.badge{position:absolute;border-radius:50%}
.badge.star{left:50px;top:444px;width:72px;height:72px;background:var(--gold);clip-path:polygon(50% 0,61% 35%,98% 35%,68% 57%,79% 91%,50% 70%,21% 91%,32% 57%,2% 35%,39% 35%);border-radius:0}
.badge.shield{left:756px;top:440px;width:52px;height:76px;background:var(--silver);border-radius:40% 40% 50% 50%}
.cta-band{position:absolute;left:0;top:512px;width:864px;height:48px;background:var(--royal);color:var(--white);font-family:'Oswald',sans-serif}
.cta-band .only{position:absolute;left:24px;top:13px;font-size:15px;white-space:nowrap}
.cta-band .call{position:absolute;right:48px;top:6px;font-size:23px;font-weight:500;display:flex;align-items:center;gap:14px;white-space:nowrap}
.cta-band .call span{display:flex;align-items:center;gap:6px}
.cta-band svg,.back-cta svg{width:20px;height:20px}

/* back */
.back-left{position:absolute;left:0;top:0;width:432px;height:560px;background:var(--paper)}
.back .brand-mark{left:14px;top:24px;width:90px;font-size:8px;line-height:1.15;gap:4px}
.back .brand-mark .dot{width:34px;height:34px;border-width:3px}
.back-title{position:absolute;left:122px;top:30px;font-family:'Oswald',sans-serif;font-weight:600;font-size:21px;color:var(--royal);white-space:nowrap}
.back-sub{position:absolute;left:120px;top:58px;font-family:'Oswald',sans-serif;font-weight:500;font-size:10px;color:var(--ink);line-height:13px}
.menu{position:absolute;left:0;top:104px;width:432px;height:332px;background:var(--royal);color:var(--white);font-family:'Open Sans',sans-serif}
.course{position:absolute;left:20px;width:310px}
.course h3{font-family:'Open Sans',sans-serif;font-weight:700;font-size:11.5px;line-height:14px}
.course p{font-size:7.2px;line-height:9.8px}
.course .price{font-weight:600}
.thumb{position:absolute;left:327px;width:90px;height:66px;border:1px solid var(--white)}
.thumb.t1{top:14px;background:linear-gradient(160deg,#1a1c22,#4b5262)}
.thumb.t2{top:93px;background:linear-gradient(180deg,#c9d6e6,#8a95a3)}
.thumb.t3{top:172px;background:linear-gradient(160deg,#aebfd8,#e9edf3)}
.thumb.t4{top:252px;background:linear-gradient(160deg,#6f8fc4,#1d2436)}
.back-band{position:absolute;left:0;top:436px;width:432px;height:44px;background:var(--navy);color:var(--white);text-align:center;font-family:'Oswald',sans-serif;font-size:12.5px;line-height:17px;padding-top:5px}
.back-band strong{font-weight:500}
.back-cta{position:absolute;left:0;top:486px;width:432px;text-align:center;font-family:'Oswald',sans-serif;color:var(--royal);font-size:22px;font-weight:500;display:flex;justify-content:center;align-items:center;gap:20px}
.back-cta span{display:flex;align-items:center;gap:6px}
.back-url{position:absolute;left:0;top:516px;width:432px;text-align:center;font-family:'Oswald',sans-serif;font-size:16px;color:var(--ink)}
.return-address{position:absolute;left:455px;top:25px;font-family:'Open Sans',sans-serif;font-size:11.5px;line-height:15px;color:#555;font-style:normal}
.stamp-box{position:absolute;left:740px;top:22px;width:96px;height:66px;border:1px solid var(--line)}
.address-lines{position:absolute;left:495px;top:248px;width:341px}
.address-lines span{display:block;height:30px;border-bottom:1px solid var(--line)}
</style>
</head>
<body>

<section class="postcard front">
  <div class="brand-mark"><span class="dot"></span>Brightwall Readiness Institute</div>
  <h1 class="front-title">SECURITY CORPORATE TRAINING</h1>
  <p class="front-sub">ON-SITE – SEMINARS – GROUP SETTINGS<br>REGULATORY &amp; COMPLIANCE</p>
  <div class="url-band">
    <span class="url">www.brightwallreadinessinstitute.org</span>
    <span class="license">State Security Training Lic #RX 4417</span>
  </div>
  <div class="hero-photo" role="img" aria-label="Close-up of a silver security badge as background"></div>
  <div class="hero-officer" role="img" aria-label="Security officer in cap, sunglasses, jacket and tie speaking into an earpiece"></div>
  <h2 class="provide">WE PROVIDE:</h2>
  <ul class="services">
    <li><svg viewBox="0 0 20 20"><rect x="2" y="4" width="13" height="13" fill="none" stroke="#1c1d4f" stroke-width="2"/><path d="M5 10l4 4 9-11" fill="none" stroke="#1c1d4f" stroke-width="2.4"/></svg>HANDCUFFING CERTIFICATIONS</li>
    <li><svg viewBox="0 0 20 20"><rect x="2" y="4" width="13" height="13" fill="none" stroke="#1c1d4f" stroke-width="2"/><path d="M5 10l4 4 9-11" fill="none" stroke="#1c1d4f" stroke-width="2.4"/></svg>PEPPER SPRAY</li>
    <li><svg viewBox="0 0 20 20"><rect x="2" y="4" width="13" height="13" fill="none" stroke="#1c1d4f" stroke-width="2"/><path d="M5 10l4 4 9-11" fill="none" stroke="#1c1d4f" stroke-width="2.4"/></svg>COMPLIANCE TRAINING</li>
    <li><svg viewBox="0 0 20 20"><rect x="2" y="4" width="13" height="13" fill="none" stroke="#1c1d4f" stroke-width="2"/><path d="M5 10l4 4 9-11" fill="none" stroke="#1c1d4f" stroke-width="2.4"/></svg>INSTRUCTOR TRAINING</li>
    <li><svg viewBox="0 0 20 20"><rect x="2" y="4" width="13" height="13" fill="none" stroke="#1c1d4f" stroke-width="2"/><path d="M5 10l4 4 9-11" fill="none" stroke="#1c1d4f" stroke-width="2.4"/></svg>CALIFORNIA GUARD CARD</li>
  </ul>
  <div class="onsite-band"><p>On-Site – We come to you – SAVE on Staff Training with our compliance &amp; training Seminars</p></div>
  <div class="badge star"></div>
  <div class="badge shield"></div>
  <div class="cta-band">
    <span class="only">THE ONLY INSTRUCTOR PROGRAM THAT ALLOWS YOU TO TEACH GSRB COURSES!</span>
    <span class="call">CALL NOW <span><svg viewBox="0 0 24 24"><path fill="#fff" d="M6.6 10.8a15 15 0 006.6 6.6l2.2-2.2c.3-.3.7-.4 1-.2 1.1.4 2.3.6 3.6.6.6 0 1 .4 1 1V20c0 .6-.4 1-1 1A17 17 0 013 4c0-.6.4-1 1-1h3.5c.6 0 1 .4 1 1 0 1.3.2 2.5.6 3.6.1.3 0 .7-.2 1z"/></svg>555-014-2290</span></span>
  </div>
</section>

<section class="postcard back">
  <div class="back-left">
    <div class="brand-mark"><span class="dot"></span>Brightwall Readiness Institute</div>
    <h2 class="back-title">SECURITY CORPORATE TRAINING</h2>
    <p class="back-sub">ON-SITE – SEMINARS – GROUP SETTINGS<br>REGULATORY &amp; COMPLIANCE</p>
    <div class="menu">
      <div class="course" style="top:4px">
        <h3>Tactical Handcuffing:</h3>
        <p class="price">$1000 for up to 20 personnel</p>
        <p>• Nomenclature - Basic Stance – Patterns of Movement – Cover and Contact Officer<br>• Practical Application – Standing – Kneeling – Prone Positions<br>• Pat Downs, Searches - Report Writing<br>• 4 hour operator training<br>• Certificates of Completion Issued Same Day</p>
      </div>
      <div class="course" style="top:83px">
        <h3>Chemical Agents (Pepper Spray)</h3>
        <p class="price">$1000 for up to 20 personnel</p>
        <p>• Defense tool – Use of Force<br>• Spraying Techniques – Disengaging – Patterns of Movement - Defense against Attacks<br>• Drawing Techniques - Deployment Considerations - Tactical Considerations<br>• Decontamination Procedures - Report Writing<br>• 4 hour operator training<br>• Certificate of Completion issued Same Day</p>
      </div>
      <div class="course" style="top:166px">
        <h3>Baton Training (Expandable) Refresher Training</h3>
        <p class="price">$1650 for up to 20 personnel <em>(NOT INCLUDING $50 BATON PERMIT FEE per Student!)</em></p>
        <p>• Prevent law suits with compliance and refresher training<br>• Use of Force<br>• Officer Safety – CA laws<br>• Striking Techniques – Defensive Techniques<br>• 4 hour operator training</p>
      </div>
      <div class="course" style="top:243px">
        <h3>Active Shooter Training</h3>
        <p class="price">$1650 for up to 20 personnel</p>
        <p>• State of the Art simulator, hundreds of real life scenarios<br>• Room Entry Tactics, Movement as a Team<br>• Clearing hallways and rooms<br>• Tactical Considerations<br>• Use of Simulator Firearms – 6 hour operator training<br>• Certificate of Training issued at end of program</p>
      </div>
      <div class="thumb t1" role="img" aria-label="Officer in uniform cap holding a flashlight"></div>
      <div class="thumb t2" role="img" aria-label="Officer standing in a parking lot"></div>
      <div class="thumb t3" role="img" aria-label="Security officer in light blue shirt in a corridor"></div>
      <div class="thumb t4" role="img" aria-label="Security officer seen from behind speaking into a radio"></div>
    </div>
    <div class="back-band">THE ONLY INSTRUCTOR PROGRAM THAT ALLOWS YOU TO TEACH GSRB COURSES!<br><strong>DON'T SETTLE FOR OUT OF STATE PROGRAMS</strong></div>
    <div class="back-cta">CALL NOW <span><svg viewBox="0 0 24 24"><path fill="#2e3192" d="M6.6 10.8a15 15 0 006.6 6.6l2.2-2.2c.3-.3.7-.4 1-.2 1.1.4 2.3.6 3.6.6.6 0 1 .4 1 1V20c0 .6-.4 1-1 1A17 17 0 013 4c0-.6.4-1 1-1h3.5c.6 0 1 .4 1 1 0 1.3.2 2.5.6 3.6.1.3 0 .7-.2 1z"/></svg>555-014-2290</span></div>
    <p class="back-url">www.brightwallreadinessinstitute.org</p>
  </div>
  <address class="return-address">Brightwall Readiness Institute<br>1820 W. Harlow Ave<br>Fairmont, CA 90000</address>
  <div class="stamp-box"></div>
  <div class="address-lines"><span></span><span></span><span></span><span></span><span></span></div>
</section>

</body>
</html>
```